The Wellness Barn Business Card

Info for the front..... (in whichever order and layout looks best)
Carla Penhallow
Physiotherapist
4/37 Upper Creekbank Rd
Tallowbrook
QLD 4712
0462305178
carlapenhallow57@mailbox.example
www.thewellnessbarn.example.au
on the back I would like to be able to write appointments so probably just that heading with lines.
I like a sort of rustic style but mostly professional, colours in naturals, beige, brown, green etc. I dont mind if the logo colour is changed slightly to suit.

```html
<!DOCTYPE html>
<html lang="en">
<head>
<meta charset="UTF-8">
<title>The Wellness Barn Business Card</title>
<link href="https://fonts.googleapis.com/css2?family=Poppins:wght@400;600;700&display=swap" rel="stylesheet">
<style>
  :root {
    --barn-green: #2d4a20;
    --card-white: #ffffff;
    --text-grey: #7a7a7a;
    --rule-grey: #b9b9b9;
    --line-light: rgba(255,255,255,0.55);
    --backdrop: #e7e6e2;
  }
  * { margin: 0; padding: 0; box-sizing: border-box; }
  html, body {
    width: 1200px; height: 952px; overflow: hidden;
    background: var(--backdrop);
    font-family: "Poppins", sans-serif;
  }
  .sheet {
    width: 1200px; height: 952px;
    display: flex; flex-direction: column;
    align-items: center; justify-content: center; gap: 70px;
  }
  .card {
    position: relative;
    width: 640px; height: 366px;
    box-shadow: 0 6px 18px rgba(0,0,0,0.18);
    overflow: hidden;
  }
  .card-front { background: var(--card-white); }
  .card-back { background: var(--barn-green); }

  .brand-mark {
    position: absolute; left: 56px; top: 66px; width: 210px;
    display: flex; align-items: center; gap: 12px;
  }
  .brand-dot {
    flex: none; width: 26px; height: 26px; border-radius: 50%;
    background: var(--barn-green);
  }
  .brand-name {
    font-weight: 700; font-size: 30px; line-height: 1.08;
    color: var(--barn-green);
  }

  .contact-block { position: absolute; left: 300px; top: 70px; width: 320px; }
  .person-name { font-weight: 700; font-size: 24px; color: var(--barn-green); line-height: 1.2; }
  .person-role { font-size: 15px; color: var(--text-grey); margin-top: 2px; }
  .role-rule { width: 46px; height: 1px; background: var(--rule-grey); margin: 8px 0 12px; }
  .contact-list { list-style: none; }
  .contact-item {
    display: flex; align-items: flex-start; gap: 9px;
    font-size: 12.5px; color: var(--text-grey); line-height: 1.35; margin-bottom: 7px;
  }
  .contact-icon { flex: none; width: 17px; height: 17px; margin-top: 1px; }

  .base-rule { position: absolute; left: 0; right: 0; bottom: 44px; height: 6px; }
  .base-rule-grey { position: absolute; left: 0; width: 44%; top: 2px; height: 2px; background: var(--rule-grey); }
  .base-rule-green { position: absolute; left: 44%; right: 0; top: 0; height: 6px; background: var(--barn-green); }

  .back-inner {
    position: absolute; inset: 34px 60px 40px;
    display: flex; flex-direction: column; align-items: center;
  }
  .back-brand { font-weight: 700; font-size: 24px; color: var(--card-white); line-height: 1.2; }
  .appointment-heading {
    margin-top: 14px;
    font-weight: 600; font-size: 15px; letter-spacing: 3px; text-transform: uppercase;
    color: var(--card-white);
  }
  .writing-lines { list-style: none; width: 100%; margin-top: 10px; }
  .writing-line { height: 40px; border-bottom: 1px solid var(--line-light); }
</style>
</head>
<body>
<main class="sheet">
  <section class="card card-front" aria-label="Card front">
    <div class="brand-mark">
      <span class="brand-dot"></span>
      <span class="brand-name">The Wellness Barn</span>
    </div>
    <div class="contact-block">
      <h1 class="person-name">Carla Penhallow</h1>
      <p class="person-role">Physiotherapist</p>
      <div class="role-rule"></div>
      <ul class="contact-list">
        <li class="contact-item">
          <svg class="contact-icon" viewBox="0 0 17 17"><rect width="17" height="17" rx="3" fill="#2d4a20"/><path d="M8.5 3.5a3.3 3.3 0 0 0-3.3 3.3c0 2.5 3.3 6.4 3.3 6.4s3.3-3.9 3.3-6.4a3.3 3.3 0 0 0-3.3-3.3z" fill="#fff"/><circle cx="8.5" cy="6.8" r="1.2" fill="#2d4a20"/></svg>
          <span>4/37 Upper Creekbank Rd Tallowbrook<br>QLD 4712</span>
        </li>
        <li class="contact-item">
          <svg class="contact-icon" viewBox="0 0 17 17"><rect width="17" height="17" rx="3" fill="#2d4a20"/><path d="M5.5 3.8l1.8-.3 1 2.6-1.2.9a6 6 0 0 0 2.9 2.9l.9-1.2 2.6 1-.3 1.8c-.1.5-.5.8-1 .8A8.2 8.2 0 0 1 4.7 4.8c0-.5.3-.9.8-1z" fill="#fff"/></svg>
          <span>0462305178</span>
        </li>
        <li class="contact-item">
          <svg class="contact-icon" viewBox="0 0 17 17"><rect width="17" height="17" rx="3" fill="#2d4a20"/><rect x="3.5" y="5" width="10" height="7" fill="none" stroke="#fff" stroke-width="1.3"/><path d="M3.5 5l5 4 5-4" fill="none" stroke="#fff" stroke-width="1.3"/></svg>
          <span>carlapenhallow57@mailbox.example</span>
        </li>
        <li class="contact-item">
          <svg class="contact-icon" viewBox="0 0 17 17"><rect width="17" height="17" rx="3" fill="#2d4a20"/><path d="M5 4l7.5 4.2-3.2.8-1.4 3.2z" fill="#fff"/></svg>
          <span>www.thewellnessbarn.example.au</span>
        </li>
      </ul>
    </div>
    <div class="base-rule">
      <span class="base-rule-grey"></span>
      <span class="base-rule-green"></span>
    </div>
  </section>

  <section class="card card-back" aria-label="Card back">
    <div class="back-inner">
      <span class="back-brand">The Wellness Barn</span>
      <h2 class="appointment-heading">Appointments</h2>
      <ul class="writing-lines">
        <li class="writing-line"></li>
        <li class="writing-line"></li>
        <li class="writing-line"></li>
        <li class="writing-line"></li>
        <li class="writing-line"></li>
      </ul>
    </div>
  </section>
</main>
</body>
</html>
```